Funeral Service App for our Client

Our client would like an app that celebrates and helps remember loved one's lives. We need an app design that provides soft tones and a peaceful feel. It should have a hero background that takes up most of the top part. It needs to provide three clickable options towards the bottom that are stacked vertically on the main page and the buttons need to seem like lables.

The first button would display another page and that page will have a collapsable search box at the top, and below it, a hero image of the deceased person. There should be a section below the image for traversing to next and previous images. Below this middle section, a text area that can hold scrollable text for an obiturary

The second button should bring up a new page (or view) that has an image list of upcoming services for that funeral home. Images should be on the left and descriptions on the right. Below each image and description should be 2 label buttons (or surprise us with a better UI) that can launch one of two pages. The left button launches the same view as the first button from the main page of the app. The right button will refresh the page with a contextual search of relatives who have also been deceased

The third button from the main page will behave like the second button but the listings will be that of affiliated funeral service providers. No label buttons below this image list but clicking the image will launch a webview page for that affiliate.

Please also include responsive designs for landscape modes

Target Market(s)

United States funeral directors

Industry/Entity Type

Professional Service

Font styles to use
Sans Serif

Colors
fac994
34a6d7
fff3d1
cee9f5

Requirements
Must have
• non platform specific design that can work equally on IOS, Android or Windows
Nice to have
• use own judgement on colors even though I provided a range

```html
<!DOCTYPE html>
<html lang="en">
<head>
<meta charset="utf-8">
<title>Upcoming Services</title>
<link rel="stylesheet" href="https://fonts.googleapis.com/css2?family=Lato:wght@300;400;700&display=swap">
<style>
  :root {
    --teal: #3fc1d6;
    --sand: #e2b483;
    --paper: #f0f0f0;
    --white: #ffffff;
    --photo-light: #66645f;
    --photo-dark: #3b3a38;
    --notch: #5a5855;
  }
  * { box-sizing: border-box; margin: 0; padding: 0; }
  html, body { width: 738px; height: 1200px; overflow: hidden; background: var(--paper); }
  body { font-family: "Lato", sans-serif; color: var(--white); }

  .screen { width: 738px; height: 1200px; display: flex; flex-direction: column; }

  .status-bar {
    height: 40px; background: var(--teal); display: flex; align-items: center;
    justify-content: space-between; padding: 0 14px; font-size: 20px; font-weight: 400;
  }
  .status-left, .status-right { display: flex; align-items: center; gap: 6px; width: 220px; }
  .status-right { justify-content: flex-end; }
  .signal { display: flex; gap: 3px; }
  .signal span { width: 10px; height: 10px; border-radius: 50%; background: var(--white); }
  .signal span.off { background: none; border: 1.5px solid var(--white); }
  .battery { width: 44px; height: 18px; border: 1.5px solid var(--white); border-radius: 3px; position: relative; padding: 2px; }
  .battery::before { content: ""; display: block; width: 22%; height: 100%; background: var(--white); }
  .battery::after { content: ""; position: absolute; right: -5px; top: 5px; width: 3px; height: 6px; background: var(--white); border-radius: 0 2px 2px 0; }

  .app-header {
    height: 82px; background: var(--teal); display: flex; align-items: center;
    justify-content: space-between; padding: 0 30px 0 36px;
  }
  .app-title { font-size: 33px; font-weight: 700; letter-spacing: 0.3px; }

  .service-list { flex: 1; display: flex; flex-direction: column; }
  .service { flex: 1; display: flex; }
  .service.reverse { flex-direction: row-reverse; }

  .portrait {
    width: 50%; position: relative;
    background: radial-gradient(ellipse at 50% 40%, var(--photo-light), var(--photo-dark) 80%);
  }
  .portrait-name {
    position: absolute; bottom: 30px; left: 0; right: 0; text-align: center;
    font-size: 32px; font-weight: 400;
  }

  .details { width: 50%; background: var(--sand); display: flex; flex-direction: column; }
  .summary { height: 182px; display: flex; flex-direction: column; align-items: center; justify-content: center; gap: 12px; padding-bottom: 8px; }
  .summary-title { font-size: 34px; font-weight: 700; }
  .summary-text { font-size: 21px; font-weight: 400; opacity: 0.9; }

  .label-button {
    height: 70px; display: flex; align-items: center; justify-content: center;
    font-size: 29px; font-weight: 400; position: relative;
  }
  .label-button + .label-button { margin-top: 11px; }
  .label-button.browse { background: var(--paper); color: var(--teal); }
  .label-button.related { background: var(--teal); color: var(--white); }
  .label-button::before {
    content: ""; position: absolute; top: 50%; transform: translateY(-50%);
    border-top: 13px solid transparent; border-bottom: 13px solid transparent;
  }
  .service .label-button::before { left: 0; border-left: 16px solid var(--notch); }
  .service.reverse .label-button::before { right: 0; border-right: 16px solid var(--notch); }
</style>
</head>
<body>
<div class="screen">
  <div class="status-bar">
    <div class="status-left">
      <div class="signal"><span></span><span></span><span></span><span class="off"></span><span class="off"></span></div>
      <span>NIMBUS</span>
      <svg width="22" height="16" viewBox="0 0 22 16" aria-hidden="true"><path d="M1 6a14 14 0 0 1 20 0M4.5 9.5a9 9 0 0 1 13 0M8 13a4 4 0 0 1 6 0" fill="none" stroke="#fff" stroke-width="2" stroke-linecap="round"/></svg>
    </div>
    <span>4:21 PM</span>
    <div class="status-right"><span>22%</span><div class="battery"></div></div>
  </div>

  <header class="app-header">
    <svg width="38" height="28" viewBox="0 0 38 28" aria-label="Menu"><path d="M1 3h36M1 14h36M1 25h36" stroke="#fff" stroke-width="3"/></svg>
    <h1 class="app-title">UPCOMING SERVICES</h1>
    <svg width="32" height="32" viewBox="0 0 32 32" aria-label="Search"><circle cx="13" cy="13" r="10.5" fill="none" stroke="#fff" stroke-width="2.4"/><path d="M21 21l9 9" stroke="#fff" stroke-width="2.6" stroke-linecap="round"/></svg>
  </header>

  <main class="service-list">
    <article class="service">
      <div class="portrait" role="img" aria-label="Portrait photo of a smiling young man with tousled hair">
        <span class="portrait-name">Name it</span>
      </div>
      <div class="details">
        <div class="summary"><h2 class="summary-title">Description</h2><p class="summary-text">more description</p></div>
        <a class="label-button browse">Browser</a>
        <a class="label-button related">Related</a>
      </div>
    </article>

    <article class="service reverse">
      <div class="portrait" role="img" aria-label="Portrait photo of a smiling woman with long wavy hair">
        <span class="portrait-name">Name it</span>
      </div>
      <div class="details">
        <div class="summary"><h2 class="summary-title">Description</h2><p class="summary-text">more description</p></div>
        <a class="label-button browse">Browser</a>
        <a class="label-button related">Related</a>
      </div>
    </article>

    <article class="service">
      <div class="portrait" role="img" aria-label="Portrait photo of a grinning man with short hair">
        <span class="portrait-name">Name it</span>
      </div>
      <div class="details">
        <div class="summary"><h2 class="summary-title">Description</h2><p class="summary-text">more description</p></div>
        <a class="label-button browse">Browser</a>
        <a class="label-button related">Related</a>
      </div>
    </article>
  </main>
</div>
</body>
</html>
```